We need a web designer/programmer for Bright Harbor Ltd in London who's primary aid is to assist young people to find activities they'd like to do in their area. the MarbleTrove is mainly a post code or key word search engine. my brief attached shows what I want the web to do and how it should look. the Friends/KoruValers page is almost like a dating site. instead of choose blond hair blue eyed, young people search for friend who's doing similar activities or wearing the same size mountain boot etc so that they could share. hope it all make sense. I really want the website to go live and launch party at the end of Sept/early Oct. hope that's realistic. Thank you. Regards, Mab

Target Market(s)

young people 14-25

Number of Pages Required

5+ page

Font styles to use
Sans Serif

Requirements
Must have
• search engine, interactive, chat, user registration. remote editing with security code for my customers.
• needs to be colourful to attract young people.
• colour match the Bright Harbor Logo
Nice to have
• matching style to the KoruVal-hub.example web

```html
<!DOCTYPE html>
<html lang="en">
<head>
<meta charset="utf-8">
<title>Bright Harbor – we nurture people</title>
<link href="https://fonts.googleapis.com/css2?family=Open+Sans:wght@400;600&display=swap" rel="stylesheet">
<style>
:root{
  --bg:#f7f7f7;
  --ink:#555;
  --muted:#888;
  --berry:#8e1a4b;
  --orange:#f6a21c;
  --amber:#ffc933;
  --pink:#c8548e;
  --green:#7dc142;
  --grey:#707070;
  --silver:#b8b8b8;
  --indigo:#5b5ea6;
  --footer:#333;
  --footer-deep:#2a2a2a;
  --lime:#8dc63f;
}
*{box-sizing:border-box;margin:0;padding:0}
html,body{width:740px;height:1200px;overflow:hidden}
body{background:var(--bg);font-family:"Open Sans",sans-serif;color:var(--ink);position:relative}
.abs{position:absolute}

.brand{left:64px;top:52px;display:flex;align-items:center;gap:8px;font-size:20px;font-weight:600;color:var(--berry)}
.brand-dot{width:22px;height:22px;border-radius:50%;background:var(--green)}

.follow{right:62px;top:32px;display:flex;align-items:center;gap:6px}
.follow-label{font-size:10.5px;line-height:14px;color:var(--muted);text-align:right;margin-right:2px}
.social{width:20px;height:20px;border-radius:50%;display:flex;align-items:center;justify-content:center}
.s-blue{background:#3b5998}.s-sky{background:#1da1f2}.s-green{background:#5aad45}.s-dark{background:#333}.s-chat{background:#25b33a}

.nav{left:293px;top:100px;width:386px;display:flex}
.nav a{flex:1 1 auto;white-space:nowrap;text-align:center;font-size:11px;color:var(--muted);text-decoration:none;padding:0 6px 9px;border-bottom:4px solid}
.nav a.current{color:#e0447a}

.hero-photo{left:61px;top:138px;width:425px;height:291px;background:linear-gradient(135deg,#cfe3f0,#e8d3bf 50%,#9fb3c6)}
.hero-panel{left:486px;top:138px;width:193px;height:291px;background:var(--berry);padding:26px 8px 0 24px}
.hero-panel h1{font-size:19px;font-weight:600;color:var(--amber);line-height:24px;white-space:nowrap}
.hero-panel h2{font-size:15.5px;font-weight:600;color:var(--amber);line-height:20px;margin-bottom:12px;white-space:nowrap}
.hero-panel p{font-size:10.5px;line-height:17px;color:#f4dbe6;width:152px}
.hero-panel p span{color:var(--amber)}
.btn{display:inline-block;margin-top:14px;background:var(--orange);color:var(--berry);font-size:11.5px;padding:7px 10px;border-radius:2px}
.dots{margin-top:22px;display:inline-flex;gap:7px;background:#5e0f30;border-radius:7px;padding:4px 6px}
.dots i{width:6px;height:6px;border-radius:50%;background:#fff}
.dots i:first-child{background:none;border:1px solid #fff}

.sec-title{font-size:13px;font-weight:600}
.pic{height:111px}
.elephants{left:61px;top:624px;width:410px;height:110px;background:linear-gradient(90deg,#d6b08c,#a88468 50%,#e4c9a9)}

.rule{left:61px;top:760px;width:410px;height:1px;background:#ddd}
.welcome{left:63px;top:776px;width:410px}
.welcome h3{font-size:18px;font-weight:600;color:var(--berry);margin-bottom:10px}
.welcome p{font-size:8.2px;line-height:14px;color:var(--muted);margin-bottom:9px}

.ads{left:486px;top:438px;width:192px;height:564px;background:#eee;border:1px solid #e2e2e2}
.tile{width:80px;height:80px}

.footer{left:0;top:1008px;width:740px;height:154px;background:var(--footer)}
.fcol{top:1016px}
.fcol h4{font-size:11.5px;font-weight:400;color:var(--lime);margin-bottom:10px}
.fcol li{list-style:none;font-size:8.6px;color:#ddd;line-height:15.5px}
.news p{font-size:8.6px;color:#bbb;line-height:12px;width:155px;margin-bottom:6px}
.field{width:152px;height:17px;background:#f2f2f2;border:1px solid #ccc;font-size:8px;color:#666;padding:2px 8px;margin-bottom:4px}
.sub{margin-left:92px;margin-top:6px;width:59px;height:17px;background:#6aa12b;color:#fff;font-size:8px;text-align:center;line-height:17px}
.fsocial{display:flex;gap:6px;margin-bottom:7px}
.copy{left:0;top:1162px;width:740px;height:38px;background:var(--footer-deep);font-size:8px;color:#999;text-align:center;line-height:38px}
</style>
</head>
<body>

<div class="abs brand"><span class="brand-dot"></span>Bright Harbor</div>

<div class="abs follow">
  <div class="follow-label">Contact us &amp;<br>Follow us on</div>
  <span class="social s-blue"></span>
  <span class="social s-sky"></span>
  <span class="social s-green"><svg width="11" height="8" viewBox="0 0 11 8"><rect x="0.5" y="0.5" width="10" height="7" fill="none" stroke="#fff"/><path d="M.5 .5 5.5 4.5 10.5 .5" fill="none" stroke="#fff"/></svg></span>
  <span class="social s-dark"><svg width="10" height="10" viewBox="0 0 10 10"><path d="M2 1 4 3 3 4.5Q4.5 6.5 5.5 7L7 6 9 8 8 9.5Q4 9.5 .5 2Z" fill="#fff"/></svg></span>
  <span class="social s-chat"></span>
</div>

<nav class="abs nav">
  <a class="current" style="border-color:var(--pink)">Home</a>
  <a style="border-color:var(--green)">AAP listing</a>
  <a style="border-color:var(--grey)">dark KoruValer</a>
  <a style="border-color:var(--berry)">Gallery</a>
  <a style="border-color:var(--silver)">AAP</a>
  <a style="border-color:var(--indigo)">Contact us</a>
</nav>

<div class="abs hero-photo" role="img" aria-label="Photo of young friends sitting together outdoors looking at a tablet"></div>
<div class="abs hero-panel">
  <h1>Bright Harbor,</h1>
  <h2>we nurture people</h2>
  <p>it doesn't matter what skin colours you have or what identity you are, we are here to help you, nurture you and to bring the best out of you@<span>bright-harbor.example</span></p>
  <div class="btn">Register Now</div><br>
  <div class="dots"><i></i><i></i><i></i><i></i></div>
</div>

<div class="abs sec-title" style="left:63px;top:446px;color:var(--berry)">AAP listing@BrightHarbor</div>
<div class="abs sec-title" style="left:273px;top:446px;color:var(--orange)">KoruValer@BrightHarbor</div>
<div class="abs pic" style="left:61px;top:468px;width:199px;background:linear-gradient(135deg,#e9e0c8,#c9a46a 50%,#8fa3b8)" role="img" aria-label="Photo of a group of students walking with folders"></div>
<div class="abs pic" style="left:272px;top:468px;width:199px;background:linear-gradient(180deg,#8ec3e8,#c9dbe8 60%,#7d9bb8)" role="img" aria-label="Photo of smiling friends giving thumbs up under a blue sky"></div>

<div class="abs sec-title" style="left:63px;top:601px;color:var(--indigo)">AAP@BrightHarbor</div>
<div class="abs elephants" role="img" aria-label="Photo of elephants walking across dusty ground"></div>

<div class="abs rule"></div>
<div class="abs welcome">
  <h3>Welcome to Bright Harbor</h3>
  <p>Aliquam eget quam dignissim, mollis turpis quis, suscipit justo. Mauris auctor nulla in nulla consectetur pulvinar. Nulla luctus mauris eleifend enim accumsan, id mollis ex sollicitudin. Curabitur hendrerit, lectus eget luctus ultrices, libero massa sollicitudin nibh, a euismod justo mi vel ante. Nam vehicula libero tempus tincidunt mollis. Morbi quis euismod lectus. Nam lacinia turpis odio, eget imperdiet erat porta ut. Sed posuere dignissim metus a gravida. Class aptent taciti sociosqu ad litora torquent per conubia nostra, per inceptos himenaeos. Cras a lorem nibh.</p>
  <p>Praesent ligula leo, molestie id faucibus ac, ultrices a magna. Suspendisse mattis iaculis felis, et vulputate diam consequat nec. Vestibulum porta rhoncus urna, id rutrum purus iaculis a. Donec id maximus eros. Morbi nec iaculis felis. Nunc nec molestie quam, sed suscipit turpis. Pellentesque iaculis lacus et arcu congue, ac pellentesque arcu viverra. Lorem ipsum dolor sit amet, consectetur adipiscing elit. Nullam quis sem et nisl lacinia condimentum. Nam hendrerit nunc orci, at condimentum leo aliquam et. Fusce vitae sagittis nisi. Maecenas nec neque quis nibh ullamcorper egestas id vel neque.</p>
</div>

<aside class="abs ads" aria-label="Advertisements"></aside>
<div class="abs tile" style="left:496px;top:450px;background:#ee6a7b" role="img" aria-label="Advert tile, pink"></div>
<div class="abs tile" style="left:587px;top:450px;background:#2ed12e" role="img" aria-label="Advert tile, green"></div>
<div class="abs tile" style="left:496px;top:540px;background:#1f3040" role="img" aria-label="Advert tile, dark blue"></div>
<div class="abs tile" style="left:587px;top:540px;background:linear-gradient(135deg,#2b4d1f,#dcdcdc)" role="img" aria-label="Advert tile, green and grey"></div>
<div class="abs tile" style="left:496px;top:630px;background:linear-gradient(180deg,#f2d26b,#9ccb4a)" role="img" aria-label="Advert tile, landscape illustration"></div>
<div class="abs tile" style="left:587px;top:630px;background:linear-gradient(180deg,#f4f4f4 75%,#f39c12 75%)" role="img" aria-label="Advert tile, white and orange"></div>
<div class="abs tile" style="left:496px;top:721px;background:linear-gradient(135deg,#d8dcd8,#6b6f6b)" role="img" aria-label="Advert tile, grey cards"></div>
<div class="abs tile" style="left:587px;top:721px;background:#e6e6e6" role="img" aria-label="Advert tile, paint palette illustration"></div>
<div class="abs tile" style="left:496px;top:812px;background:linear-gradient(180deg,#444,#222)" role="img" aria-label="Advert tile, dark"></div>
<div class="abs tile" style="left:587px;top:812px;background:#3cbac8" role="img" aria-label="Advert tile, teal"></div>
<div class="abs tile" style="left:496px;top:902px;background:radial-gradient(circle,#111 62%,#eee 63%)" role="img" aria-label="Advert tile, black circle"></div>
<div class="abs tile" style="left:587px;top:902px;background:linear-gradient(180deg,#c8102e 40%,#fff 40%,#fff 80%,#111 80%)" role="img" aria-label="Advert tile, red white and black"></div>

<footer class="abs footer"></footer>
<div class="abs fcol" style="left:72px">
  <h4>Quick Links</h4>
  <ul><li>Home</li><li>AAP listing</li><li>dark KoruValer</li><li>Gallery</li><li>AAP</li><li>Contact us</li></ul>
</div>
<div class="abs fcol" style="left:179px">
  <h4>Support Links</h4>
  <ul><li>Clients</li><li>Partners</li><li>Testimonials</li><li>Jobs</li><li>Categories</li></ul>
</div>
<div class="abs fcol" style="left:289px">
  <h4>Support Links</h4>
  <ul><li>Press</li><li>Legal Notice</li><li>Privacy Policy</li><li>Term of Use</li></ul>
</div>
<div class="abs fcol news" style="left:399px">
  <h4>Newsletters Sign Up</h4>
  <p>Sign up for our daily email by entering your information below</p>
  <div class="field">Your name</div>
  <div class="field">Email address</div>
  <div class="sub">SUBSCRIBE</div>
</div>
<div class="abs fcol" style="left:588px">
  <h4>Connect With Us</h4>
  <div class="fsocial">
    <span class="social s-blue"></span><span class="social s-sky"></span>
    <span class="social s-green"><svg width="11" height="8" viewBox="0 0 11 8"><rect x="0.5" y="0.5" width="10" height="7" fill="none" stroke="#fff"/><path d="M.5 .5 5.5 4.5 10.5 .5" fill="none" stroke="#fff"/></svg></span>
  </div>
  <div class="fsocial">
    <span class="social" style="background:#555"><svg width="10" height="10" viewBox="0 0 10 10"><path d="M2 1 4 3 3 4.5Q4.5 6.5 5.5 7L7 6 9 8 8 9.5Q4 9.5 .5 2Z" fill="#fff"/></svg></span>
    <span class="social s-chat"></span>
  </div>
</div>
<div class="abs copy">Copyright © 2014 Bright Harbor. All rights reserved.</div>

</body>
</html>
```